Progressive/contemporary business card design for successful Startups as a Service Company

New logo launched in 2020. New website launched in 2021. Now that COVID is (mostly) behind us, I'm networking with more people and need a business card that matches the company/logo design aesthetic.

```html
<!DOCTYPE html>
<html lang="en">
<head>
<meta charset="utf-8">
<title>Northlane Business Card</title>
<link rel="stylesheet" href="https://fonts.googleapis.com/css2?family=Montserrat:wght@300;400;500;600&display=swap">
<style>
  :root {
    --stage: #24242b;
    --card: #1e1e20;
    --card-back: #151516;
    --white: #f2f2f2;
    --blue: #2ea3dc;
    --orange: #f08a24;
    --grey: #d8d8d8;
    --deco-start: #1c8fd6;
    --deco-mid: #b62aa8;
    --deco-end: #6cc23b;
  }
  html, body {
    margin: 0;
    width: 1200px;
    height: 800px;
    overflow: hidden;
    background: var(--stage);
    font-family: "Montserrat", sans-serif;
  }
  .canvas {
    position: relative;
    width: 1200px;
    height: 800px;
  }
  .card {
    position: absolute;
    top: 250px;
    width: 525px;
    height: 300px;
    border-radius: 22px;
    overflow: hidden;
    box-shadow: 0 14px 30px rgba(0,0,0,0.45);
  }
  .card-front { left: 50px; background: var(--card); }
  .card-back { left: 625px; background: var(--card-back); }

  .front-decoration {
    position: absolute;
    right: 0;
    top: 0;
    width: 215px;
    height: 300px;
    background: linear-gradient(160deg, var(--deco-start) 0%, var(--deco-mid) 50%, var(--deco-end) 100%);
    opacity: 0.9;
  }
  .brand {
    position: absolute;
    left: 36px;
    top: 58px;
    display: flex;
    align-items: center;
    gap: 12px;
  }
  .brand-name {
    font-size: 27px;
    font-weight: 400;
    letter-spacing: 5px;
    color: var(--white);
  }
  .brand-square {
    width: 16px;
    height: 16px;
    background: var(--white);
  }
  .person {
    position: absolute;
    left: 36px;
    top: 160px;
  }
  .person-name {
    margin: 0;
    font-size: 15px;
    font-weight: 500;
    letter-spacing: 1px;
    color: var(--white);
  }
  .person-title {
    margin: 2px 0 12px;
    font-size: 12px;
    font-weight: 500;
    letter-spacing: 0.5px;
    color: var(--blue);
  }
  .contact-list {
    list-style: none;
    margin: 0;
    padding: 0;
  }
  .contact-item {
    display: flex;
    align-items: center;
    gap: 9px;
    margin-bottom: 6px;
    font-size: 12.5px;
    color: var(--grey);
  }
  .contact-icon { width: 12px; height: 12px; flex: none; }

  .back-pattern {
    position: absolute;
    inset: 0;
    background: linear-gradient(135deg, #121213, #1b1b1d);
  }
  .back-brand {
    position: absolute;
    right: 48px;
    top: 70px;
    display: flex;
    align-items: center;
    gap: 8px;
  }
  .back-brand .brand-name { font-size: 14px; letter-spacing: 3px; }
  .back-brand .brand-square { width: 10px; height: 10px; }
</style>
</head>
<body>
<main class="canvas">
  <section class="card card-front">
    <div class="front-decoration" role="img" aria-label="Colourful faceted brand decoration in blue, magenta and green"></div>
    <div class="brand">
      <span class="brand-name">NORTHLANE</span>
      <span class="brand-square"></span>
    </div>
    <div class="person">
      <p class="person-name">DANA REYES</p>
      <p class="person-title">MANAGING DIRECTOR</p>
      <ul class="contact-list">
        <li class="contact-item">
          <svg class="contact-icon" viewBox="0 0 12 12"><path d="M2 1h3l1 3-1.5 1a6 6 0 0 0 2.5 2.5L8 6l3 1v3a1 1 0 0 1-1 1A9 9 0 0 1 1 2a1 1 0 0 1 1-1z" fill="var(--orange)"/></svg>
          <span>555-014-2207</span>
        </li>
        <li class="contact-item">
          <svg class="contact-icon" viewBox="0 0 12 12"><rect x="1" y="2.5" width="10" height="7" rx="1" fill="var(--orange)"/><path d="M1.5 3l4.5 3.5L10.5 3" stroke="var(--card)" fill="none"/></svg>
          <span>dana@northlane.co</span>
        </li>
        <li class="contact-item">
          <svg class="contact-icon" viewBox="0 0 12 12"><circle cx="6" cy="6" r="5" fill="var(--orange)"/><path d="M1 6h10M6 1c2 2 2 8 0 10M6 1c-2 2-2 8 0 10" stroke="var(--card)" stroke-width="0.8" fill="none"/></svg>
          <span>www.northlane.co</span>
        </li>
      </ul>
    </div>
  </section>

  <section class="card card-back">
    <div class="back-pattern" role="img" aria-label="Black embossed lattice pattern covering the card back"></div>
    <div class="back-brand">
      <span class="brand-name">NORTHLANE</span>
      <span class="brand-square"></span>
    </div>
  </section>
</main>
</body>
</html>
```